New Property management company business cards

Looking for a new business card, to reflect new younger ownership
Card should be clean, simple and professional but with a modern layout that is conveys our new logo and business model

Key aspects of the business:

Property Management
Facility Maintenance
Project Management
Tenant Improvements

Mailing Address:
PO BOX 7816
Larkdale CA, 95418

Phone: 209-418-6071
Direct: 209-418-6074

Doyle Marsh
President

Target Market(s)

Commercial property owners

Industry/Entity Type

Real Estate property management

Contact Information for Business Card

Open to all designs but lean toward vertical layouts

Requirements
Must have
• Logo and space to customize name and contact info

```html
<!DOCTYPE html>
<html lang="en">
<head>
<meta charset="utf-8">
<title>Halbrook Property Management – Business Card</title>
<link rel="stylesheet" href="https://fonts.googleapis.com/css2?family=Montserrat:wght@400;500;600&display=swap">
<style>
  :root {
    --ink: #302f3e;
    --teal: #22b0a8;
    --paper: #ffffff;
    --backdrop: #3b3b3e;
  }
  * { box-sizing: border-box; margin: 0; padding: 0; }
  html, body { width: 1200px; height: 1200px; overflow: hidden; }
  body {
    background: var(--backdrop);
    font-family: "Montserrat", sans-serif;
    position: relative;
  }
  .card {
    position: absolute;
    left: 250px;
    width: 700px;
    height: 400px;
    border-radius: 28px;
    overflow: hidden;
    box-shadow: 0 14px 30px rgba(0,0,0,0.35);
    background: var(--ink);
  }
  .card--front { top: 150px; }
  .card--back { top: 650px; }

  .front-top {
    position: absolute; left: 0; top: 0; width: 100%; height: 238px;
    background: var(--paper);
  }
  .front-rule {
    position: absolute; left: 0; top: 218px; width: 100%; height: 9px;
    background: var(--teal);
  }
  .brand {
    position: absolute; left: 0; width: 100%;
    text-align: center;
    font-weight: 600;
    letter-spacing: 0.08em;
  }
  .brand__name { display: block; font-size: 44px; line-height: 1; }
  .brand__sub { display: block; font-size: 14px; letter-spacing: 0.42em; margin-top: 10px; }
  .card--front .brand { top: 80px; color: var(--ink); }
  .card--back .brand { top: 140px; color: var(--paper); }

  .person {
    position: absolute; left: 60px; bottom: 56px;
  }
  .person__name {
    color: var(--teal); font-weight: 600; font-size: 38px;
    letter-spacing: -0.01em; text-transform: uppercase; line-height: 1;
  }
  .person__title {
    color: var(--paper); font-size: 16px; font-weight: 500;
    text-transform: uppercase; margin-top: 6px;
  }
  .contact {
    position: absolute; left: 410px; top: 262px;
    list-style: none; color: var(--paper);
    font-size: 17px; font-weight: 500; line-height: 1.2;
  }
  .contact li { display: flex; align-items: flex-start; gap: 10px; margin-bottom: 6px; }
  .contact svg { width: 18px; height: 18px; flex: none; margin-top: 1px; fill: var(--teal); }

  .back-bar {
    position: absolute; right: 0; bottom: 48px;
    width: 360px; height: 18px; background: var(--teal);
  }
</style>
</head>
<body>
  <section class="card card--front">
    <div class="front-top"></div>
    <div class="front-rule"></div>
    <div class="brand">
      <span class="brand__name">HALBROOK</span>
      <span class="brand__sub">PROPERTY MANAGEMENT</span>
    </div>
    <div class="person">
      <p class="person__name">Doyle Marsh</p>
      <p class="person__title">President</p>
    </div>
    <ul class="contact">
      <li>
        <svg viewBox="0 0 24 24" aria-hidden="true"><path d="M6.6 10.8a15 15 0 0 0 6.6 6.6l2.2-2.2c.3-.3.7-.4 1-.2 1.1.4 2.3.6 3.6.6.6 0 1 .4 1 1V20c0 .6-.4 1-1 1A17 17 0 0 1 3 4c0-.6.4-1 1-1h3.5c.6 0 1 .4 1 1 0 1.2.2 2.4.6 3.6.1.3 0 .7-.2 1z"/></svg>
        <span>209-418-6071</span>
      </li>
      <li>
        <svg viewBox="0 0 24 24" aria-hidden="true"><path d="M7 1h10a2 2 0 0 1 2 2v18a2 2 0 0 1-2 2H7a2 2 0 0 1-2-2V3a2 2 0 0 1 2-2zm0 3v15h10V4zm5 16.2a1 1 0 1 0 0 .01z"/></svg>
        <span>209-418-6074</span>
      </li>
      <li>
        <svg viewBox="0 0 24 24" aria-hidden="true"><path d="M12 2a7 7 0 0 0-7 7c0 5 7 13 7 13s7-8 7-13a7 7 0 0 0-7-7zm0 9.5A2.5 2.5 0 1 1 12 6.5a2.5 2.5 0 0 1 0 5z"/></svg>
        <span>PO BOX 7816<br>Larkdale CA, 95418</span>
      </li>
    </ul>
  </section>

  <section class="card card--back">
    <div class="brand">
      <span class="brand__name">HALBROOK</span>
      <span class="brand__sub">PROPERTY MANAGEMENT</span>
    </div>
    <div class="back-bar"></div>
  </section>
</body>
</html>
```